Redcliff Oil & Gas Exploration, LLC

Our website (www.redcliffoilandgas.example) is poorly done and dated. I want to redo it with one main page and wide format photos or oil & gas drilling and production. Perhaps all of the pages listed on the left side of the existing site could be viewed by scrolling down further on the new main page. I want something clean and easy to navigate.

Target Market(s)

Other oil and gas companies and people that we have contacted regarding selling or leasing their mineral rights. These people will come to our website to research our company and become more comfortable doing business with us.

Industry/Entity Type

Oil And Gas

Coding

Coded - Design and coding required

Number of Pages Required

1 page

Font styles to use
Serif

Requirements
Must have
• Clean and uncluttered. Nice, clear wide format picture or oil well or rig and landscape.

```html
<!DOCTYPE html>
<html lang="en">
<head>
<meta charset="utf-8">
<title>Redcliff Oil &amp; Gas Exploration, LLC</title>
<link href="https://fonts.googleapis.com/css2?family=Tinos:wght@400;700&family=Open+Sans:wght@400;600;700&display=swap" rel="stylesheet">
<style>
:root{
  --orange:#e8601c;
  --yellow:#f9c21d;
  --ink:#1f1f1f;
  --muted:#8a8a8a;
  --grey-bg:#ececec;
  --footer-bg:#e6e6e6;
  --white:#ffffff;
  --dark-band:#1d2530;
  --serif:"Tinos","Times New Roman",serif;
  --sans:"Open Sans",Arial,sans-serif;
}
*{box-sizing:border-box;margin:0;padding:0}
html,body{width:1200px;height:3087px;overflow:hidden;background:var(--white)}
body{position:relative;font-family:var(--sans);color:var(--ink)}
.abs{position:absolute}
.btn{position:absolute;height:30px;border-radius:15px;font:700 11px/30px var(--sans);text-align:center;color:var(--white)}
.btn-yellow{background:var(--yellow)}
.btn-orange{background:var(--orange)}
.section-title{position:absolute;font:700 27px/1.2 var(--serif);color:var(--ink)}
.section-title::after{content:"";display:block;width:52px;height:2px;background:var(--yellow);margin-top:14px}

/* header */
.site-header{position:absolute;left:0;top:0;width:1200px;height:95px;background:var(--white)}
.brand{position:absolute;left:78px;top:20px;display:flex;align-items:center;gap:8px}
.brand-dot{width:30px;height:30px;border-radius:50%;background:var(--orange)}
.brand-name{font:700 31px/1 var(--serif);color:var(--ink)}
.brand-sub{position:absolute;left:118px;top:56px;font:700 10px var(--serif);color:var(--ink)}
.main-nav{position:absolute;top:38px;left:368px;display:flex;gap:24px;font:400 12px var(--sans);color:#333}
.main-nav .active{color:var(--orange);position:relative}
.main-nav .active::before{content:"";position:absolute;left:-4px;right:-4px;top:-8px;height:2px;background:var(--orange)}
.phone-box{position:absolute;left:828px;top:30px;width:124px;height:34px;border-top:1px solid #333;border-bottom:1px solid #333;font:700 15px/32px var(--serif);text-align:center}

/* hero */
.hero{position:absolute;left:0;top:95px;width:1200px;height:481px;background:linear-gradient(180deg,#d9561c 0%,#f08a2c 45%,#e2701f 62%,#9a3a10 100%)}
.hero-title{position:absolute;left:155px;top:170px;font:700 34px var(--serif);color:var(--white)}
.hero-sub{position:absolute;left:155px;top:212px;font:400 27px var(--sans);color:var(--white)}

/* about */
.about-text{position:absolute;left:383px;top:636px;width:505px;font:400 15.5px/1.45 var(--serif);color:var(--ink)}
.about-small{position:absolute;left:383px;top:742px;width:480px;font:400 11.5px/1.65 var(--sans);color:var(--muted)}
.founder-name{position:absolute;left:915px;top:636px;font:400 15px var(--serif);color:var(--yellow)}
.founder-role{position:absolute;left:915px;top:658px;font:400 11px var(--sans);color:#555}
.founder-rule{position:absolute;left:915px;top:680px;width:50px;height:1px;background:var(--yellow)}

/* projects */
.projects{position:absolute;left:0;top:960px;width:1200px;height:527px;background:var(--grey-bg)}
.stat-big{position:absolute;left:156px;top:1290px;font:700 22px var(--serif)}
.stat-note{position:absolute;left:156px;top:1318px;width:190px;font:400 10px/1.3 var(--sans);color:#333}
.card{position:absolute;top:1025px;width:205px;height:388px;background:var(--white)}
.card-photo{height:200px;background:linear-gradient(180deg,#5f8fb8,#d2874a)}
.card-label{position:absolute;left:0;top:145px;width:100%;height:55px;background:rgba(40,30,25,.72);padding:10px 24px}
.card-name{font:400 15px var(--serif);color:var(--yellow)}
.card-role{font:600 10px var(--sans);color:var(--white)}
.card-text{padding:14px 24px;font:400 11.5px/1.6 var(--sans);color:var(--muted)}
.card-dot{position:absolute;left:26px;bottom:-14px;width:28px;height:28px;border-radius:50%;background:var(--white);box-shadow:0 1px 4px rgba(0,0,0,.2)}
.card-dot.on{background:var(--orange)}
.card-dot::after{content:"+";position:absolute;width:100%;text-align:center;font:700 14px/28px var(--sans);color:var(--orange)}
.card-dot.on::after{color:var(--white)}

/* stats band */
.stats{position:absolute;left:0;top:1487px;width:1200px;height:278px;background:linear-gradient(180deg,#2a3442,#141a22)}
.stat{position:absolute;top:1555px;width:200px;text-align:center;color:var(--white)}
.stat-ring{width:100px;height:100px;margin:0 auto;border-radius:50%;border:2px solid rgba(255,255,255,.85);display:flex;align-items:center;justify-content:center}
.stat-ring.filled{background:var(--orange);border-color:var(--orange)}
.stat-title{margin-top:14px;font:400 16px var(--serif)}
.stat-sub{font:400 11px var(--sans)}

/* offer */
.offer{position:absolute;left:0;top:1765px;width:1200px;height:520px;background:linear-gradient(180deg,#ffffff,#f1f1f1)}
.offer-item{position:absolute;width:200px}
.offer-icon{width:42px;height:42px;border-radius:50%;background:var(--yellow);display:flex;align-items:center;justify-content:center}
.offer-title{margin-top:18px;font:400 15px var(--serif)}
.offer-text{font:400 11px/1.45 var(--sans);color:var(--muted)}

/* testimonial */
.testimonial{position:absolute;left:0;top:2285px;width:1200px;height:412px;background:linear-gradient(180deg,#2c3035,#1c1f24)}
.quote-text{position:absolute;left:240px;top:2398px;width:720px;text-align:center;font:italic 400 13.5px/1.55 var(--sans);color:var(--white)}
.avatar{position:absolute;border-radius:50%;background:#8c7b6d;border:3px solid var(--white)}
.person-name{position:absolute;left:500px;top:2602px;width:200px;text-align:center;font:400 15px var(--serif);color:var(--white)}
.person-role{position:absolute;left:500px;top:2624px;width:200px;text-align:center;font:400 10px var(--sans);color:#ddd}

/* contact */
.contact-text{position:absolute;left:383px;top:2757px;width:670px;font:400 15.5px/1.5 var(--serif)}
.call{position:absolute;left:383px;top:2830px;font:400 22px var(--serif);display:flex;align-items:center;gap:10px}
.email{position:absolute;left:637px;top:2836px;font:400 12px var(--sans);color:var(--muted);display:flex;align-items:center;gap:6px}

/* footer */
.site-footer{position:absolute;left:0;top:2975px;width:1200px;height:112px;background:var(--footer-bg)}
.footer-brand{position:absolute;left:160px;top:3007px;width:34px;height:34px;border-radius:50%;background:var(--orange)}
.footer-copy{position:absolute;left:206px;top:3012px;font:400 12px/1.5 var(--sans);color:#333}
.footer-links{position:absolute;left:648px;top:3024px;font:400 11px var(--sans);color:#333}
.social{position:absolute;top:3017px;width:30px;height:30px;border-radius:50%;border:1px solid #999}
.social.on{background:var(--orange);border-color:var(--orange)}
</style>
</head>
<body>

<header class="site-header">
  <div class="brand"><span class="brand-dot"></span><span class="brand-name">Redcliff</span></div>
  <div class="brand-sub">Oil &amp; Gas Exploration, LLC</div>
  <nav class="main-nav">
    <span class="active">History</span><span>Team</span><span>Available Prospects</span><span>Location</span><span>Contact Us</span>
  </nav>
  <div class="phone-box">&#9742; 555.014.2290</div>
  <div class="btn btn-yellow" style="left:1007px;top:32px;width:112px">Get a Quote</div>
</header>

<section class="hero" role="img" aria-label="Wide photo of offshore oil platforms silhouetted against an orange sunset sea"></section>
<div class="hero-title">Independent</div>
<div class="hero-sub">Oil &amp; Gad Exploration</div>
<div class="btn btn-yellow" style="left:155px;top:368px;width:128px">Explore More</div>

<section class="about">
  <div class="abs" role="img" aria-label="Faint pumpjack silhouette" style="left:150px;top:790px;width:210px;height:170px;background:linear-gradient(180deg,rgba(0,0,0,0),rgba(0,0,0,.05))"></div>
  <h2 class="section-title" style="left:156px;top:632px">About Us</h2>
  <p class="about-text">Redcliff Oil &amp; Gas Exploration, LLC was founded in 2011 by Daniel Marlow. Redcliff has expanded their business, and currently has offices located in Fort Worth and Oklahoma City.</p>
  <p class="about-small">Since 2012 Redcliff has acquired more than 25,000 net acres of leasehold in Texas, Oklahoma and Kansas. During the same time, the company has also purchased in excess of 10,000 mineral acres primarily in Oklahoma and to a lesser extent, East Texas. In addition, Redcliff has participated in hundreds of wells with top tier operators.</p>
  <div class="btn btn-orange" style="left:383px;top:866px;width:128px">Discover More</div>
  <div class="founder-name">Daniel Marlow</div>
  <div class="founder-role">Founder</div>
  <div class="founder-rule"></div>
  <div class="abs" role="img" aria-label="Founder's handwritten signature" style="left:915px;top:705px;width:70px;height:55px;background:#f3f3f3"></div>
</section>

<section class="projects"></section>
<h2 class="section-title" style="left:156px;top:1017px">Our Projects<br>&amp; Team</h2>
<div class="abs" role="img" aria-label="Yellow map of the United States with office location pins" style="left:156px;top:1135px;width:200px;height:120px;background:var(--yellow);border-radius:14px"></div>
<div class="stat-big">411k</div>
<div class="stat-note">Average barrels of oil equivalent (working interest production) per day during 2017</div>

<article class="card" style="left:383px">
  <div class="card-photo" role="img" aria-label="Photo of the founder in a hard hat at an oil site"></div>
  <div class="card-label"><div class="card-name">Daniel Marlow</div><div class="card-role">Founder</div></div>
  <p class="card-text">Daniel has been an independent landman since 2005. Since starting Redcliff, he has successfully put ...</p>
  <span class="card-dot"></span>
</article>
<article class="card" style="left:612px">
  <div class="card-photo" role="img" aria-label="Photo of the manager in a white hard hat"></div>
  <div class="card-label"><div class="card-name">Walter Marlow</div><div class="card-role">Manager</div></div>
  <p class="card-text">Walter has over 35 years of experience as a petroleum geologist. He was most recently the East Texas Exploration ...</p>
  <span class="card-dot on"></span>
</article>
<article class="card" style="left:840px">
  <div class="card-photo" role="img" aria-label="Photo of the partner in a pink hard hat and safety vest"></div>
  <div class="card-label"><div class="card-name">Owen Pryce</div><div class="card-role">Partner</div></div>
  <p class="card-text">Owen spent seven years at Keystone Energy, managing commercial real estate transactions. He left in January of 2012 ...</p>
  <span class="card-dot"></span>
</article>

<section class="stats" role="img" aria-label="Dark photo of an oil refinery at dusk"></section>
<div class="stat" style="left:157px">
  <div class="stat-ring"><svg width="36" height="36" viewBox="0 0 36 36"><circle cx="18" cy="18" r="16" fill="#fff"/><path d="M10 12c4 0 5 3 8 3s2 5-1 6-3 5-5 5M22 8c2 3 6 4 6 8" stroke="#1d2530" stroke-width="2" fill="none"/></svg></div>
  <div class="stat-title">Expanding Provider</div><div class="stat-sub">of Industrial Solutions</div>
</div>
<div class="stat" style="left:386px">
  <div class="stat-ring filled"><svg width="30" height="36" viewBox="0 0 30 36"><path d="M4 2h22v32l-11-9-11 9z" fill="#fff"/></svg></div>
  <div class="stat-title">Global Certificate</div><div class="stat-sub">ISO 9001:2015</div>
</div>
<div class="stat" style="left:616px">
  <div class="stat-ring"><svg width="44" height="34" viewBox="0 0 44 34"><circle cx="22" cy="9" r="7" fill="#fff"/><circle cx="9" cy="12" r="5" fill="#fff"/><circle cx="35" cy="12" r="5" fill="#fff"/><path d="M10 34c0-10 24-10 24 0zM0 30c0-8 14-8 14-3v3zM44 30c0-8-14-8-14-3v3z" fill="#fff"/></svg></div>
  <div class="stat-title">600+ Redcliff</div><div class="stat-sub">Oil &amp; Gas Exploration Staff</div>
</div>
<div class="stat" style="left:843px">
  <div class="stat-ring"><svg width="40" height="34" viewBox="0 0 40 34"><path d="M2 34V4h8v14l10-8v8l10-8v24z" fill="#fff"/></svg></div>
  <div class="stat-title">Leading Provider</div><div class="stat-sub">Gas &amp; Oil Industry</div>
</div>

<section class="offer"></section>
<div class="abs" role="img" aria-label="Faint pumpjack silhouettes across the background" style="left:330px;top:2050px;width:860px;height:230px;background:linear-gradient(180deg,rgba(0,0,0,0),rgba(0,0,0,.04))"></div>
<h2 class="section-title" style="left:156px;top:1832px">What We<br>Offer</h2>

<div class="offer-item" style="left:383px;top:1838px">
  <div class="offer-icon"><svg width="22" height="24" viewBox="0 0 22 24"><path d="M11 1L4 23M11 1l7 22M6 8h10M5 14h12" stroke="#222" stroke-width="2" fill="none"/></svg></div>
  <div class="offer-title">Thermal Power</div>
  <p class="offer-text">On the other hand, we denounce with righteous indignation and dislike men who are ...</p>
</div>
<div class="offer-item" style="left:611px;top:1838px">
  <div class="offer-icon"><svg width="24" height="20" viewBox="0 0 24 20"><path d="M3 14a9 9 0 0 1 18 0zM1 14h22v3H1z" fill="#222"/></svg></div>
  <div class="offer-title">Oil Platform</div>
  <p class="offer-text">So blinded by desire, that they cannot foresee the pain and trouble that are bound ...</p>
</div>
<div class="offer-item" style="left:840px;top:1838px">
  <div class="offer-icon"><svg width="20" height="24" viewBox="0 0 20 24"><path d="M10 2c6 7 7 11 7 14a7 7 0 0 1-14 0c0-3 1-7 7-14z" fill="none" stroke="#222" stroke-width="2"/></svg></div>
  <div class="offer-title">Gas Flaring</div>
  <p class="offer-text">To those who fail in their duty through weakness of will, which is the same as saying ...</p>
</div>
<div class="offer-item" style="left:383px;top:2015px">
  <div class="offer-icon"><svg width="24" height="22" viewBox="0 0 24 22"><path d="M2 6l18-4M8 5v17M14 22L8 8M18 4v8" stroke="#222" stroke-width="2" fill="none"/></svg></div>
  <div class="offer-title">Oil Pump</div>
  <p class="offer-text">He rejects pleasures to secure other greater pleasures, or else he endures pains to ...</p>
</div>
<div class="offer-item" style="left:611px;top:2015px">
  <div class="offer-icon"><svg width="22" height="22" viewBox="0 0 22 22"><path d="M2 2h18v18H2zM2 9h18" stroke="#222" stroke-width="2" fill="none"/></svg></div>
  <div class="offer-title">Oil Refinery</div>
  <p class="offer-text">When our power of choice is untrammeled and when nothing prevents our being able ...</p>
</div>
<div class="offer-item" style="left:840px;top:2015px">
  <div class="offer-icon"><svg width="22" height="22" viewBox="0 0 22 22"><path d="M2 21V3h7v6h6V6h5v15z" stroke="#222" stroke-width="2" fill="none"/></svg></div>
  <div class="offer-title">Factory</div>
  <p class="offer-text">Obligations of business frequently occur that pleasures have to be repudiated and annoyances ...</p>
</div>
<div class="btn btn-yellow" style="left:383px;top:2192px;width:128px">Explore More</div>

<section class="testimonial" role="img" aria-label="Dark photo of refinery towers"></section>
<svg class="abs" style="left:573px;top:2350px" width="54" height="34" viewBox="0 0 54 34"><path d="M2 2h20v18l-8 12H6l6-12H2zM32 2h20v18l-8 12h-8l6-12H32z" fill="none" stroke="#f9c21d" stroke-width="3"/></svg>
<p class="quote-text">There are many variations of passages of Lorem Ipsum available, but the majority have suffered alteration in some form, by injected humour, or randomised words which don't look even slightly believable. If you are going to use a passage of Lorem Ipsum, you need to be sure there isn't anything embarrassing hidden in the middle of text. All the Lorem Ipsum generators on the Internet tend to repeat ...</p>
<svg class="abs" style="left:118px;top:2468px" width="14" height="26" viewBox="0 0 14 26"><path d="M12 2L2 13l10 11" stroke="#fff" stroke-width="2" fill="none"/></svg>
<svg class="abs" style="left:1068px;top:2468px" width="14" height="26" viewBox="0 0 14 26"><path d="M2 2l10 11L2 24" stroke="#e8601c" stroke-width="2" fill="none"/></svg>
<div class="avatar" role="img" aria-label="Client portrait" style="left:480px;top:2531px;width:50px;height:50px"></div>
<div class="avatar" role="img" aria-label="Featured client portrait" style="left:562px;top:2515px;width:76px;height:76px"></div>
<div class="avatar" role="img" aria-label="Client portrait" style="left:668px;top:2531px;width:50px;height:50px"></div>
<div class="person-name">Lorem Ipsum</div>
<div class="person-role">Dummy Text</div>

<section class="contact">
  <h2 class="section-title" style="left:156px;top:2757px">Contact Us</h2>
  <p class="contact-text">We're always interested in new projects, big or small. Please don't hesitate to get in touch with us regarding your project.</p>
  <div class="call"><svg width="22" height="22" viewBox="0 0 24 24"><path d="M6 2l4 5-2 3c1 3 3 5 6 6l3-2 5 4-2 4C10 22 2 14 2 4z" fill="#222"/></svg>Call: 555.014.2290</div>
  <div class="email"><svg width="14" height="10" viewBox="0 0 14 10"><rect x="0.5" y="0.5" width="13" height="9" fill="none" stroke="#8a8a8a"/><path d="M1 1l6 5 6-5" stroke="#8a8a8a" fill="none"/></svg>inquiry@redcliffoilandgas.example</div>
  <div class="btn btn-yellow" style="left:383px;top:2885px;width:112px">Get a Quote</div>
</section>

<footer class="site-footer"></footer>
<span class="footer-brand"></span>
<div class="footer-copy">© 2017 <b>Redcliff</b> Oil &amp; Gas Exploration, LLC<br><span style="color:#888;font-size:11px">All RightReserved.</span></div>
<div class="footer-links">Contact Us &nbsp;|&nbsp; Privacy Policy &nbsp;|&nbsp; Sitemap</div>
<span class="social" style="left:902px"></span>
<span class="social on" style="left:940px"></span>
<span class="social" style="left:978px"></span>
<span class="social" style="left:1014px"></span>

</body>
</html>
```